Tech business card design

We need an amazing business card design for our new business 'Brakka' a marketing tech startup based in Sydney, Australia. We provide an online marketplace for businesses to search and buy advertising media, connect with service providers and learn more about marketing. We wish to communicate 'cool tech', reliability and professionalism and design based around our logo.

Target Market(s)

Business Owners

Contact Information for Business Card

Name
Position
Email Address
Website
Phone Number

Font styles to use
Other font styles liked:
• Avenir & Avenir Next

Colors

Designer to choose colors to be used in the design.

```html
<!DOCTYPE html>
<html lang="en">
<head>
<meta charset="utf-8">
<title>Brakka Business Card</title>
<link rel="stylesheet" href="https://fonts.googleapis.com/css2?family=Nunito+Sans:wght@300;400;700&display=swap">
<style>
  :root {
    --navy: #14143c;
    --paper: #ffffff;
    --ink-grey: #6e6e73;
    --soft-grey: #8c8c90;
    --backdrop: #cfcfd1;
  }
  * { margin: 0; padding: 0; box-sizing: border-box; }
  html, body {
    width: 1200px;
    height: 800px;
    overflow: hidden;
  }
  body {
    background: var(--backdrop);
    font-family: "Nunito Sans", "Avenir Next", Avenir, sans-serif;
    position: relative;
  }
  .card {
    position: absolute;
    top: 251px;
    width: 520px;
    height: 298px;
    border-radius: 3px;
    box-shadow: 0 6px 18px rgba(0, 0, 0, 0.18);
  }
  .card--front {
    left: 60px;
    background: var(--navy);
    display: flex;
    align-items: center;
    justify-content: center;
  }
  .card--back {
    left: 620px;
    background: var(--paper);
  }
  .wordmark {
    font-weight: 700;
    letter-spacing: -0.02em;
    line-height: 1;
  }
  .card--front .wordmark {
    color: var(--paper);
    font-size: 112px;
  }
  .card--back .wordmark {
    position: absolute;
    right: 42px;
    top: 150px;
    color: var(--navy);
    font-size: 56px;
  }
  .holder {
    position: absolute;
    left: 44px;
    top: 50px;
  }
  .holder__name {
    color: var(--navy);
    font-weight: 700;
    font-size: 22px;
    letter-spacing: 0.01em;
    text-transform: uppercase;
    line-height: 1.1;
  }
  .holder__role {
    color: var(--ink-grey);
    font-weight: 400;
    font-size: 17px;
    line-height: 1.15;
  }
  .address {
    position: absolute;
    left: 44px;
    top: 150px;
    color: var(--soft-grey);
    font-weight: 300;
    font-size: 14.5px;
    line-height: 1.35;
  }
  .contacts {
    position: absolute;
    left: 44px;
    top: 200px;
    list-style: none;
    color: var(--ink-grey);
    font-weight: 400;
    font-size: 14.5px;
  }
  .contacts li {
    display: flex;
    align-items: center;
    gap: 7px;
    height: 21px;
  }
  .contacts svg {
    width: 15px;
    height: 15px;
    flex: none;
  }
</style>
</head>
<body>
  <section class="card card--front">
    <span class="wordmark">brakka</span>
  </section>

  <section class="card card--back">
    <div class="holder">
      <p class="holder__name">Daniel Reeve</p>
      <p class="holder__role">President and CEO</p>
    </div>

    <p class="address">214 Keller St., Marlow<br>ON Canada K2P4R8</p>

    <ul class="contacts">
      <li>
        <svg viewBox="0 0 16 16" aria-hidden="true">
          <rect width="16" height="16" rx="3" fill="#14143c"/>
          <path d="M5 3.5 L6.8 5.6 L5.9 6.8 C6.6 8.2 7.8 9.4 9.2 10.1 L10.4 9.2 L12.5 11 L11.4 12.5 C7.4 12.2 3.8 8.6 3.5 4.6 Z" fill="#fff"/>
        </svg>
        <span>+34-955-410-072</span>
      </li>
      <li>
        <svg viewBox="0 0 16 16" aria-hidden="true">
          <rect width="16" height="16" rx="3" fill="#14143c"/>
          <rect x="3" y="4.5" width="10" height="7" fill="none" stroke="#fff" stroke-width="1.2"/>
          <path d="M3 4.5 L8 8.8 L13 4.5" fill="none" stroke="#fff" stroke-width="1.2"/>
        </svg>
        <span>info@brakkamail.com</span>
      </li>
      <li>
        <svg viewBox="0 0 16 16" aria-hidden="true">
          <rect width="16" height="16" rx="3" fill="#14143c"/>
          <circle cx="8" cy="8" r="4.6" fill="none" stroke="#fff" stroke-width="1.2"/>
          <ellipse cx="8" cy="8" rx="2" ry="4.6" fill="none" stroke="#fff" stroke-width="1"/>
          <line x1="3.4" y1="8" x2="12.6" y2="8" stroke="#fff" stroke-width="1"/>
        </svg>
        <span>www.brakkaweb.com</span>
      </li>
    </ul>

    <span class="wordmark">brakka</span>
  </section>
</body>
</html>
```